Software engineering company needs business card

I need a cool business card. Company: Soft Belan Brindlewood Ave 41 58207 Larkford Name: Gerald Vanholt CEO / Managing Director & Owner

```html
<!DOCTYPE html>
<html lang="en">
<head>
<meta charset="utf-8">
<title>Soft Belan – Business Card</title>
<link rel="stylesheet" href="https://fonts.googleapis.com/css2?family=Open+Sans:wght@400;600;700&display=swap">
<style>
  :root {
    --page-bg: #e8e6e2;
    --card-white: #ffffff;
    --charcoal: #4a4a4a;
    --charcoal-dark: #3f3f3f;
    --lime: #86d02a;
    --text-dark: #3a3a3a;
    --text-body: #2e2e2e;
  }
  * { box-sizing: border-box; margin: 0; padding: 0; }
  html, body {
    width: 1200px;
    height: 900px;
    overflow: hidden;
    background: var(--page-bg);
    font-family: "Open Sans", Arial, sans-serif;
  }
  .canvas {
    position: relative;
    width: 1200px;
    height: 900px;
  }
  .card {
    position: absolute;
    left: 294px;
    width: 612px;
    height: 350px;
    box-shadow: 0 6px 18px rgba(0,0,0,0.18);
    overflow: hidden;
  }
  /* Back side */
  .card-back {
    top: 60px;
    background: var(--charcoal);
    display: flex;
    align-items: center;
    justify-content: center;
  }
  .brand {
    display: flex;
    align-items: center;
    gap: 14px;
  }
  .brand-square {
    width: 22px;
    height: 22px;
  }
  .brand-name {
    font-size: 40px;
    font-weight: 600;
    letter-spacing: 0.04em;
    line-height: 1;
    white-space: nowrap;
  }
  .card-back .brand-square { background: var(--card-white); }
  .card-back .brand-name { color: var(--card-white); }

  /* Front side */
  .card-front {
    top: 490px;
    background: var(--card-white);
  }
  .front-shapes {
    position: absolute;
    inset: 0;
  }
  .holder {
    position: absolute;
    left: 64px;
    top: 12px;
    color: var(--text-dark);
  }
  .holder-name {
    font-size: 19px;
    font-weight: 700;
    letter-spacing: 0.02em;
    line-height: 1.15;
  }
  .holder-title {
    font-size: 13px;
    font-weight: 400;
    margin-top: 1px;
  }
  .contact-list {
    position: absolute;
    left: 30px;
    top: 124px;
    list-style: none;
    color: var(--text-body);
    font-size: 14px;
    line-height: 21px;
  }
  .contact-item {
    display: flex;
    align-items: center;
    gap: 8px;
  }
  .contact-icon {
    width: 11px;
    height: 11px;
    fill: var(--text-dark);
    flex: none;
  }
  .company-address {
    position: absolute;
    left: 30px;
    top: 194px;
    font-style: normal;
    color: var(--text-body);
    font-size: 14px;
    line-height: 19px;
  }
  .company-name { font-weight: 700; }
  .card-front .brand {
    position: absolute;
    left: 330px;
    top: 152px;
  }
  .card-front .brand-square { background: var(--lime); }
  .card-front .brand-name { color: var(--charcoal); }
</style>
</head>
<body>
<main class="canvas">

  <section class="card card-back" aria-label="Card back">
    <div class="brand">
      <span class="brand-square"></span>
      <span class="brand-name">Soft Belan</span>
    </div>
  </section>

  <section class="card card-front" aria-label="Card front">
    <svg class="front-shapes" width="612" height="350" viewBox="0 0 612 350" aria-hidden="true">
      <polygon points="0,10 24,10 10,42 0,42" fill="var(--lime)"/>
      <polygon points="30,10 56,10 56,42 16,42" fill="var(--charcoal)"/>
      <polygon points="0,264 226,264 214,292 0,292" fill="var(--lime)"/>
      <polygon points="238,300 612,300 612,350 220,350" fill="var(--charcoal-dark)"/>
    </svg>

    <header class="holder">
      <h1 class="holder-name">GERALD VANHOLT</h1>
      <p class="holder-title">CEO / Managing Director &amp; Owner</p>
    </header>

    <ul class="contact-list">
      <li class="contact-item">
        <svg class="contact-icon" viewBox="0 0 12 12" aria-hidden="true"><path d="M1 3.5C1 2 2.5 1.5 6 1.5S11 2 11 3.5V5H8.5V4H3.5V5H1z M2.5 6h7l1 4.5h-9z"/></svg>
        <span>(555)014-2280</span>
      </li>
      <li class="contact-item">
        <svg class="contact-icon" viewBox="0 0 12 12" aria-hidden="true"><path d="M0.5 2.5h11v7h-11z M1.5 3.5v0.4L6 7l4.5-3.1v-0.4z" fill-rule="evenodd"/></svg>
        <span>info@softbelan.example</span>
      </li>
      <li class="contact-item">
        <svg class="contact-icon" viewBox="0 0 12 12" aria-hidden="true"><circle cx="6" cy="6" r="5.5"/></svg>
        <span>www.softbelan.example</span>
      </li>
    </ul>

    <address class="company-address">
      <span class="company-name">Soft Belan</span><br>
      Brindlewood Ave 41<br>
      58207 Larkford
    </address>

    <div class="brand">
      <span class="brand-square"></span>
      <span class="brand-name">Soft Belan</span>
    </div>
  </section>

</main>
</body>
</html>
```